Pitch Deck Redesign

Our company is currently in need of our pitch deck to be revamped and made much cleaner. We have a solid foundation and framework and now just need a final polishing.
We are looking to hire a freelance graphic designer that we can create a long-term relationship with. We want to be able to utilize this person week after week for various projects and designs. Designs will need to be delivered to our team both as png that will slide ride into a wide view powerpoint presentation and will need to supply original design file (PSD).
Thank you in advance for your responses and time,
Niles
It Company

```html
<!DOCTYPE html>
<html lang="en">
<head>
<meta charset="utf-8">
<title>Meet our great team</title>
<link rel="stylesheet" href="https://fonts.googleapis.com/css2?family=Roboto:wght@300;400;700&display=swap">
<style>
  :root {
    --bg: #45b0dc;
    --white: #ffffff;
    --photo: #e8e7ec;
    --footer: #1d4a63;
    --deco-light: #3c9fd8;
    --deco-dark: #1a63c4;
  }
  * { margin: 0; padding: 0; box-sizing: border-box; }
  html, body { width: 1200px; height: 674px; overflow: hidden; }
  body { font-family: "Roboto", Arial, sans-serif; color: var(--white); background: var(--bg); }
  .slide { position: relative; width: 1200px; height: 674px; background: var(--bg); overflow: hidden; }
  .slide-title {
    position: absolute; left: 108px; top: 108px;
    font-size: 66px; font-weight: 300; letter-spacing: -0.5px; line-height: 1;
  }
  .slide-title strong { font-weight: 700; }
  .group-label {
    position: absolute; top: 220px;
    font-size: 20px; font-weight: 700; letter-spacing: 0.2px;
  }
  .member { position: absolute; top: 255px; width: 200px; }
  .member-photo { width: 193px; height: 173px; background: var(--photo); }
  .member-name { margin-top: 12px; font-size: 20px; font-weight: 700; line-height: 24px; }
  .member-role { font-size: 20px; font-weight: 300; line-height: 24.5px; }
  .member-role b, .member-past b { font-weight: 700; }
  .member-past { margin-top: 10px; font-size: 14px; font-weight: 300; line-height: 18px; }
  .member-past.spaced { margin-top: 34px; }
  .footer {
    position: absolute; left: 28px; top: 633px;
    font-size: 12.5px; color: var(--footer); font-weight: 400;
  }
  .footer b { font-weight: 700; }
  .deco { position: absolute; right: 0; bottom: 0; }
</style>
</head>
<body>
<main class="slide">
  <h1 class="slide-title">Meet our great <strong>team</strong></h1>

  <h2 class="group-label" style="left:110px">FOUNDER</h2>
  <h2 class="group-label" style="left:367px">CORE TEAM</h2>

  <section class="member" style="left:110px">
    <div class="member-photo" role="img" aria-label="Portrait photo of Martin Dorran"></div>
    <p class="member-name">Martin Dorran</p>
    <p class="member-role"><b>Vantrel</b> | CEO</p>
    <p class="member-past"><b>Northgate Bank</b> | Senior VP<br><b>Harbor Seed Angels</b> |<br>Technology consultant<br><b>Westfield University</b> | Masters<br>in Engineering</p>
  </section>

  <section class="member" style="left:367px">
    <div class="member-photo" role="img" aria-label="Portrait photo of Selim Arvan"></div>
    <p class="member-name">Selim Arvan</p>
    <p class="member-role"><b>Vantrel</b> | Head of<br>Software Dev.</p>
    <p class="member-past"><b>KL</b> | Lead software architect</p>
  </section>

  <section class="member" style="left:624px">
    <div class="member-photo" role="img" aria-label="Portrait photo of Evan Moretti"></div>
    <p class="member-name">Evan Moretti</p>
    <p class="member-role"><b>Vantrel</b> | Head of<br>Eng. Services</p>
    <p class="member-past"><b>Calder Labs</b> |<br>Manufacturing manager</p>
  </section>

  <section class="member" style="left:882px">
    <div class="member-photo" role="img" aria-label="Portrait photo of Niles Dorran"></div>
    <p class="member-name">Niles Dorran</p>
    <p class="member-role"><b>Vantrel</b> | Lead<br>Growth Hacker</p>
    <p class="member-past"><b>Brightline Agency</b> |<br>Marketing consultant</p>
  </section>

  <p class="footer"><b>Vantrel Technology</b> | martin@vantrel.com</p>

  <svg class="deco" width="210" height="186" viewBox="0 0 210 186" role="img" aria-label="Blue watercolour brush stroke with a faint network pattern">
    <defs>
      <linearGradient id="decoFill" x1="0" y1="0" x2="1" y2="1">
        <stop offset="0" stop-color="var(--deco-light)"/>
        <stop offset="1" stop-color="var(--deco-dark)"/>
      </linearGradient>
    </defs>
    <path d="M210 0 L210 186 L0 186 C40 150 70 120 100 90 C130 60 170 30 210 0 Z" fill="url(#decoFill)" opacity="0.85"/>
  </svg>
</main>
</body>
</html>
```